Letterhead and Envelopes design using existing logo. Logo can be found at tlventures.net

Use existing logo (attached) and incorporate in letterhead and envelope designs.

Current logo can be viewed at tlventures.net the web site reflect various parent and sub companies. Please see attached as well.

Target Market(s)

Other oil and gas operators.

Industry/Entity Type

Oil And Gas

Font styles to use
Sans Serif

Colors

Designer to choose colors to be used in the design.

Requirements
Must have
• Current logo and address
Nice to have
• Modern, contemporary approach yet incorporate existing traditional design.
• After design is selected for Ridgemont Caldera Holdings I will use similar design for Royalties, Exploration, Energy and Farms with different color schemes.

```html
<!DOCTYPE html>
<html lang="en">
<head>
<meta charset="utf-8">
<title>Ridgemont Caldera Holdings – Stationery</title>
<link href="https://fonts.googleapis.com/css2?family=Poppins:wght@300;400;500&family=Roboto:wght@400&display=swap" rel="stylesheet">
<style>
  :root{
    --bg:#dcdcdc;
    --paper:#f1f1f1;
    --paper-edge:#e8e8e8;
    --ink:#222222;
    --text:#4a4a4a;
    --muted:#555555;
    --green:#6b983a;
    --rule:#9a9a9a;
    --sig:#2a5aa8;
  }
  *{box-sizing:border-box;margin:0;padding:0}
  html,body{width:1200px;height:877px;overflow:hidden;background:var(--bg)}
  body{position:relative;font-family:"Poppins",sans-serif;color:var(--text)}
  .sheet{position:absolute;background:linear-gradient(90deg,#f7f7f7,var(--paper-edge));box-shadow:0 2px 10px rgba(0,0,0,.12)}
  .letterhead{left:69px;top:64px;width:527px;height:742px}
  .brand{position:absolute;display:flex;align-items:center;gap:8px}
  .brand-dot{flex:none;border-radius:50%;background:var(--green)}
  .brand-name{font-family:"Poppins",sans-serif;font-weight:500;color:var(--ink);line-height:1.15}
  .letterhead .brand{left:37px;top:117px;top:34px;width:150px}
  .letterhead .brand-dot{width:34px;height:34px}
  .letterhead .brand-name{font-size:11px}
  .contact{position:absolute;left:369px;top:44px;padding-left:8px;border-left:1px solid var(--rule);font-family:"Roboto",sans-serif;font-size:8px;line-height:9.6px;color:var(--muted)}
  .contact .addr{margin-bottom:6px}
  .contact li{list-style:none;display:flex;align-items:center;gap:5px;line-height:10.4px}
  .contact svg{width:7px;height:7px;fill:var(--green)}
  .salutation{position:absolute;left:45px;top:208px;font-size:14px;font-weight:300;color:var(--muted)}
  .body-copy{position:absolute;left:45px;top:246px;width:440px;font-size:7.9px;line-height:11.4px;font-weight:300;color:var(--text);text-align:justify}
  .body-copy p{margin-bottom:11.4px}
  .closing{position:absolute;left:45px;top:484px;font-size:8px;font-weight:300}
  .signature{position:absolute;left:41px;top:518px;width:94px;height:40px;background:linear-gradient(90deg,rgba(42,90,168,.18),rgba(42,90,168,.08));border-radius:4px}
  .envelope-back{left:614px;top:268px;width:530px;height:242px}
  .flap{position:absolute;left:0;top:0;width:530px;height:90px}
  .envelope-back .brand{left:50%;top:34px;transform:translateX(-50%);width:200px;justify-content:center}
  .envelope-back .brand-dot{width:18px;height:18px;background:var(--ink)}
  .envelope-back .brand-name{font-size:9px;white-space:nowrap}
  .envelope-front{left:614px;top:562px;width:533px;height:242px}
  .envelope-front .brand{left:26px;top:24px;width:150px}
  .envelope-front .brand-dot{width:30px;height:30px}
  .envelope-front .brand-name{font-size:10px}
  .envelope-front .return{position:absolute;left:27px;top:104px;font-family:"Roboto",sans-serif;font-size:7.6px;line-height:9.6px;color:var(--muted)}
</style>
</head>
<body>
  <section class="sheet letterhead">
    <div class="brand">
      <span class="brand-dot"></span>
      <span class="brand-name">Ridgemont Caldera Holdings</span>
    </div>
    <div class="contact">
      <p class="addr">PO Box 318 Minot<br>North Dakota 58702</p>
      <ul>
        <li><svg viewBox="0 0 10 10"><path d="M2 0.5 3.8 2.6 2.8 3.8Q4 6.2 6.2 7.2L7.4 6.2 9.5 8 8.2 9.5Q1 8 0.5 1.8Z"/></svg>(701) 555.0142</li>
        <li><svg viewBox="0 0 10 10"><path d="M0 2h10v6H0z"/></svg>reception@tlventures.net</li>
        <li><svg viewBox="0 0 10 10"><circle cx="5" cy="5" r="5"/></svg>www.tlventures.net</li>
      </ul>
    </div>
    <h1 class="salutation">Dear Mr. Carver,</h1>
    <div class="body-copy">
      <p>Lorem ipsum dolor sit amet, consectetur adipiscing elit. Donec orci purus, luctus vitae dignissim eu, iaculis sed purus. Vivamus faucibus, ipsum nec aliquet viverra, leo mauris condimentum ligula, sit amet sagittis enim ligula quis arcu. Nam egestas tortor id nisi porttitor mattis. In tortor ante, ultricies in suscipit a, tempus non massa. Vivamus et auctor mi. Fusce vel massa nulla. Phasellus nec eros mauris, et scelerisque orci.</p>
      <p>Donec malesuada orci vitae nulla accumsan porta a id massa. Quisque accumsan iaculis magna sit amet fringilla. Maecenas consequat, magna eget tincidunt semper, odio nibh rutrum mi, id feugiat ante nisi eu risus. Vestibulum nunc orci, rhoncus a placerat in, ultricies in mi. Cras mattis varius eros, vel fringilla nisi suscipit eget. Quisque scelerisque sagittis nulla at porttitor.</p>
      <p>Sed id augue vitae urna euismod commodo aliquet a quam. Pellentesque arcu velit, cursus et malesuada ut, consequat et diam. Nullam erat sem, rhoncus id ullamcorper vitae, rhoncus et arcu. In ultricies ultricies nulla, ut rutrum nisi iaculis at. Donec eu magna a metus ornare faucibus. Fusce aliquet faucibus ultricies. Morbi semper, est id tincidunt gravida, sem arcu adipiscing lacus, ac bibendum nulla leo eu purus. Quisque nec diam sed risus consectetur a ccumsan quis quis nibh. Vestibulum id purus lorem.</p>
      <p>It is a long established fact that a reader will be distracted by the readable content of a page when looking at its layout. The point of using Lorem Ipsum is that it has a more-or-less normal distribution of letters, as opposed to using 'Content here, content here', making it look like readable English. Many desktop publishing packages</p>
    </div>
    <p class="closing">Sincerely,</p>
    <div class="signature" role="img" aria-label="Handwritten signature"></div>
  </section>

  <section class="sheet envelope-back">
    <svg class="flap" viewBox="0 0 530 90" aria-hidden="true">
      <path d="M0 0H530L522 55Q516 88 480 89H50Q16 88 10 55Z" fill="var(--green)"/>
    </svg>
    <div class="brand">
      <span class="brand-dot"></span>
      <span class="brand-name">Ridgemont Caldera Holdings</span>
    </div>
  </section>

  <section class="sheet envelope-front">
    <div class="brand">
      <span class="brand-dot"></span>
      <span class="brand-name">Ridgemont Caldera Holdings</span>
    </div>
    <p class="return">PO Box 318 Minot<br>North Dakota 58702</p>
  </section>
</body>
</html>
```